When Rivers Burn, Tivendel Book Two

We need a book cover design for a basic 9x6 trim hardcover and paperback matching the general style of our first book. Black background mainly that's visually interesting with some colorful wrap-around element that goes from the front cover, over the spine, and ends on the back. Relevant colors to the book are black, gold, green, and purple. See attached cover of book one for style. This is a medieval inspired, epic fantasy featuring thrones, sieges, and adventure. We do not want a character on the cover as the focal point.

```html
<!DOCTYPE html>
<html lang="en">
<head>
<meta charset="utf-8">
<title>Beneath Our Banners – Book Cover Wrap</title>
<link rel="stylesheet" href="https://fonts.googleapis.com/css2?family=Cinzel:wght@400;500&family=Cinzel+Decorative:wght@400;700&display=swap">
<style>
  :root {
    --night: #17102a;
    --deep-violet: #2c1f4c;
    --violet: #5a4484;
    --lilac: #a08cc0;
    --wine: #6a2438;
    --ember: #c8641e;
    --amber: #e39a3a;
    --gold: #e8c66a;
    --gold-light: #f6e3a0;
    --gold-dark: #b8893a;
    --ivory: #f3ead2;
    --speck-green: #5fd04a;
  }
  * { margin: 0; padding: 0; box-sizing: border-box; }
  html, body { width: 1200px; height: 846px; overflow: hidden; background: var(--night); }

  .cover-wrap {
    position: relative;
    width: 1200px;
    height: 846px;
    overflow: hidden;
    font-family: "Cinzel", serif;
    color: var(--gold);
  }

  .marble-art {
    position: absolute;
    inset: 0;
    background:
      radial-gradient(ellipse 300px 120px at 250px 40px, rgba(224,150,58,0.85), transparent 70%),
      radial-gradient(ellipse 160px 90px at 420px 80px, rgba(200,100,30,0.55), transparent 70%),
      radial-gradient(ellipse 280px 170px at 1080px 560px, rgba(224,140,50,0.8), transparent 70%),
      radial-gradient(ellipse 260px 180px at 540px 470px, rgba(160,140,192,0.45), transparent 70%),
      radial-gradient(ellipse 320px 160px at 960px 300px, rgba(90,68,132,0.65), transparent 70%),
      radial-gradient(ellipse 320px 120px at 300px 300px, rgba(106,36,56,0.55), transparent 70%),
      radial-gradient(ellipse 260px 140px at 150px 180px, rgba(90,68,132,0.5), transparent 70%),
      linear-gradient(160deg, var(--deep-violet) 0%, var(--night) 45%, var(--deep-violet) 70%, var(--night) 100%);
  }
  .marble-veins { position: absolute; inset: 0; width: 1200px; height: 846px; }

  .back-cover, .front-cover, .spine { position: absolute; top: 0; height: 846px; text-align: center; }
  .back-cover { left: 0; width: 600px; }
  .back-tagline {
    position: absolute; left: 0; width: 610px; top: 90px;
    font-size: 16px; text-transform: uppercase; color: var(--gold);
  }
  .back-blurb {
    position: absolute; left: 78px; width: 444px;
    font-size: 12.4px; line-height: 16.2px;
    text-transform: uppercase; letter-spacing: -0.1px;
    color: var(--gold);
  }
  .back-blurb.first { top: 151px; }
  .back-blurb.second { top: 384px; }
  .back-closing {
    position: absolute; left: 140px; width: 300px; top: 532px;
    font-size: 15px; line-height: 19.5px; color: var(--ivory);
  }

  .spine { left: 578px; width: 42px; }
  .spine-volume {
    position: absolute; left: 0; width: 42px; top: 120px;
    font-size: 25px; color: var(--gold);
  }
  .spine-title, .spine-author {
    position: absolute; left: 10px;
    writing-mode: vertical-rl;
    font-family: "Cinzel Decorative", serif;
    color: var(--gold); white-space: nowrap;
  }
  .spine-title { top: 289px; font-size: 15px; }
  .spine-author { top: 648px; font-size: 15px; }

  .front-cover { left: 620px; width: 580px; }
  .gold-text {
    background: linear-gradient(180deg, var(--gold-light) 0%, var(--gold) 45%, var(--gold-dark) 100%);
    -webkit-background-clip: text; background-clip: text; color: transparent;
  }
  .front-title {
    position: absolute; left: 0; width: 580px; top: 76px;
    font-family: "Cinzel Decorative", serif; font-weight: 400;
    font-size: 54px; line-height: 104px; white-space: nowrap;
  }
  .front-author {
    position: absolute; left: 0; width: 580px; top: 676px;
    font-family: "Cinzel Decorative", serif;
    font-size: 34px; letter-spacing: 1px; white-space: nowrap;
  }
</style>
</head>
<body>
<main class="cover-wrap">
  <div class="marble-art" role="img" aria-label="Fluid marble artwork in deep purple and black with a continuous gold and ember vein wrapping from the front, across the spine, to the back, dusted with green speckles">
    <svg class="marble-veins" viewBox="0 0 1200 846" aria-hidden="true">
      <defs>
        <linearGradient id="vein-gold" x1="0" y1="0" x2="1" y2="0">
          <stop offset="0" stop-color="#c8641e"/>
          <stop offset="0.35" stop-color="#e8b04a"/>
          <stop offset="0.6" stop-color="#f0c060"/>
          <stop offset="1" stop-color="#e38a32"/>
        </linearGradient>
        <filter id="soft" x="-10%" y="-50%" width="120%" height="200%"><feGaussianBlur stdDeviation="6"/></filter>
        <filter id="softer" x="-10%" y="-50%" width="120%" height="200%"><feGaussianBlur stdDeviation="18"/></filter>
      </defs>
      <path d="M0 500 C120 470 220 520 330 560 S520 560 600 585 S760 640 860 560 S1040 470 1200 520"
            fill="none" stroke="url(#vein-gold)" stroke-width="60" opacity="0.45" filter="url(#softer)"/>
      <path d="M0 500 C120 470 220 520 330 560 S520 560 600 585 S760 640 860 560 S1040 470 1200 520"
            fill="none" stroke="url(#vein-gold)" stroke-width="12" opacity="0.9" filter="url(#soft)"/>
      <path d="M0 690 C80 700 160 690 260 680 S420 690 500 700"
            fill="none" stroke="#e0b070" stroke-width="4" opacity="0.6" filter="url(#soft)"/>
      <path d="M830 50 C900 30 960 55 1020 40 S1110 30 1140 28"
            fill="none" stroke="#e8c890" stroke-width="5" opacity="0.75" filter="url(#soft)"/>
      <g fill="var(--speck-green)" opacity="0.85">
        <circle cx="1050" cy="650" r="2"/><circle cx="1080" cy="700" r="1.5"/><circle cx="1120" cy="660" r="2.5"/>
        <circle cx="1145" cy="720" r="2"/><circle cx="1100" cy="760" r="1.5"/><circle cx="1170" cy="690" r="3"/>
        <circle cx="1010" cy="740" r="1.5"/><circle cx="1060" cy="790" r="2"/><circle cx="1140" cy="800" r="1.5"/>
        <circle cx="950" cy="800" r="3"/><circle cx="900" cy="770" r="1.5"/><circle cx="980" cy="690" r="1.5"/>
        <circle cx="730" cy="685" r="3"/><circle cx="760" cy="720" r="1.5"/><circle cx="690" cy="740" r="1.5"/>
        <circle cx="935" cy="78" r="2.5"/><circle cx="995" cy="75" r="2"/><circle cx="870" cy="130" r="1.5"/>
        <circle cx="30" cy="285" r="2"/><circle cx="60" cy="560" r="1.5"/><circle cx="20" cy="620" r="2"/>
        <circle cx="90" cy="600" r="1.5"/><circle cx="240" cy="650" r="1.5"/><circle cx="420" cy="600" r="1.5"/>
        <circle cx="560" cy="255" r="2"/><circle cx="595" cy="330" r="1.5"/><circle cx="620" cy="610" r="1.5"/>
      </g>
    </svg>
  </div>

  <section class="back-cover">
    <p class="back-tagline">Lorem ipsum dolor sit amet, consectetur.</p>
    <p class="back-blurb first">Lorem ipsum dolor sit amet, consectetur adipiscing elit. Integer fringilla libero a turpis viverra vehicula. Sed ac pellentesque ligula, ac pharetra justo. Donec ut erat vitae tortor accumsan convallis. Aenean ornare commodo purus sed semper. Sed fermentum et mi ac condimentum. Etiam sed sagittis ex, in imperdiet urna. Cras iaculis ante et purus molestie lacinia. Mauris id dolor et velit tempus imperdiet sit amet vel arcu. Class aptent taciti sociosqu ad litora torquent per conubia nostra, per inceptos himenaeos. Vivamus interdum venenatis quam. Fusce ullamcorper at arcu ut placerat. Nulla facilisi.</p>
    <p class="back-blurb second">Lorem ipsum dolor sit amet, consectetur adipiscing elit. Maecenas tristique tortor in interdum pretium. Suspendisse ultrices gravida bibendum. Etiam luctus lacus purus, sit amet elementum mi lacinia eget. Suspendisse id sem nisl. Ut lectus mi, feugiat ut tristique ut, ultricies luctus mi. Praesent id vehicula ante. Aliquam et nunc nulla.</p>
    <p class="back-closing">ULTRICES GRAVIDA BIBENDUM.<br>ETIAM LUCTUS</p>
  </section>

  <section class="spine">
    <p class="spine-volume">II</p>
    <p class="spine-title">Beneath Our Banners</p>
    <p class="spine-author">R.L. Marlow</p>
  </section>

  <section class="front-cover">
    <h1 class="front-title gold-text">BENEATH OUR<br>BANNERS</h1>
    <p class="front-author gold-text">R.L. MARLOW</p>
  </section>
</main>
</body>
</html>
```